Tidewater Cardio annual holiday card

This is our annual christmas card that will be mailed out to our patients. We are a cardiology physician clinic. Size of the card is 8 inches in width and 5 inches in height. I need a blank white space in the bottom right corner of the back of the card measuring at least 3 1/2 inch in width and 3 inches in height for address and postage to be placed. It should include our group photo, logo, address, phone, fax, and web address. Our address is 718 Marwick Ave. Ste. B, Webster, TX 77341. Phone is 832-617-2283, Fax is 832-617-2284. Web address is www.tidewatercardio-example.com. We would like it to say "Happy Holidays from the Physicians and Staff at Tidewater Cardio".
Should be able to post the same on website and social media with holiday message

Target Market(s)

Patients and doctors

Industry/Entity Type

Healthcare

Font styles to use
Script

Requirements
Must have
• Group photo with all staff included in front, logo, address, phone, fax, website. perhaps getting a wall somewhere in the back but not must
Nice to have
• some sort of holiday message or quote
Should not have
• Do not say Merry Christmas. Do not put any santa hats on people.

```html
<!DOCTYPE html>
<html lang="en">
<head>
<meta charset="utf-8">
<title>Tidewater Cardio Holiday Card</title>
<link rel="stylesheet" href="https://fonts.googleapis.com/css2?family=Great+Vibes&family=Norican&family=Montserrat:wght@400;600;700&display=swap">
<style>
  :root {
    --canvas: #9a9a9a;
    --red-deep: #8f0f18;
    --red: #c81d28;
    --red-bright: #d9252f;
    --white: #ffffff;
    --ink: #1a1a1a;
    --band: #0d0d0d;
  }
  * { margin: 0; padding: 0; box-sizing: border-box; }
  html, body { width: 1200px; height: 1200px; overflow: hidden; }
  body {
    background: var(--canvas);
    font-family: "Montserrat", sans-serif;
    position: relative;
  }
  .card { position: absolute; background: var(--white); box-shadow: 0 6px 18px rgba(0,0,0,.35); overflow: hidden; }
  .card-front { left: 184px; top: 78px; width: 832px; height: 518px; }
  .card-back { left: 184px; top: 604px; width: 832px; height: 518px; }

  .front-backdrop {
    position: absolute; left: 0; top: 0; width: 832px; height: 470px;
    background: radial-gradient(ellipse at 55% 40%, var(--red-bright) 0%, var(--red) 45%, var(--red-deep) 100%);
  }
  .group-photo {
    position: absolute; left: 48px; top: 150px; width: 740px; height: 290px;
    background: linear-gradient(180deg, #4a3a3a 0%, #2a2224 55%, #d9d9dc 100%);
    border-radius: 4px;
  }
  .snow-fade {
    position: absolute; left: 0; top: 380px; width: 832px; height: 100px;
    background: linear-gradient(180deg, rgba(255,255,255,0) 0%, var(--white) 80%);
  }
  .greeting {
    position: absolute; left: 0; top: 14px; width: 832px;
    text-align: center; color: var(--white);
  }
  .greeting-small {
    display: block;
    font-family: "Montserrat", sans-serif; font-weight: 600; font-size: 17px;
    letter-spacing: 4px; line-height: 1;
  }
  .greeting-script {
    display: block; margin-top: 2px;
    font-family: "Great Vibes", cursive; font-size: 104px; line-height: 1.05;
  }

  .brand { position: absolute; display: flex; align-items: center; gap: 10px; }
  .brand-dot { width: 22px; height: 22px; border-radius: 50%; flex: none; }
  .brand-name { font-family: "Montserrat", sans-serif; font-weight: 700; font-size: 24px; line-height: 1.1; }
  .front-brand { left: 34px; top: 452px; }
  .front-brand .brand-dot { background: var(--red); }
  .front-brand .brand-name { color: var(--red); }

  .contact { position: absolute; font-size: 14px; color: var(--ink); }
  .contact-row { display: flex; align-items: center; gap: 8px; white-space: nowrap; }
  .contact-row + .contact-row { margin-top: 6px; }
  .contact-item { display: inline-flex; align-items: center; gap: 7px; margin-right: 12px; }
  .contact .strong { font-weight: 700; }
  .icon { width: 17px; height: 17px; flex: none; }
  .front-contact { left: 324px; top: 452px; }
  .front-address { left: 626px; top: 452px; display: flex; gap: 8px; font-size: 14px; line-height: 1.3; }

  .back-panel {
    position: absolute; left: 0; top: 0; width: 469px; height: 518px;
    background: radial-gradient(ellipse at 70% 50%, var(--red-bright) 0%, var(--red) 45%, var(--red-deep) 100%);
  }
  .back-brand { left: 206px; top: 94px; }
  .back-brand .brand-dot { background: var(--band); }
  .back-brand .brand-name { color: var(--band); }
  .back-message { position: absolute; left: 0; width: 469px; text-align: center; color: var(--white); font-family: "Norican", cursive; }
  .back-message .headline { position: absolute; left: 0; width: 100%; top: 196px; font-size: 58px; line-height: 1; }
  .back-message .line { position: absolute; left: 0; width: 100%; font-size: 30px; line-height: 1; }
  .back-message .line-one { top: 286px; }
  .back-message .line-two { top: 334px; }
  .back-band {
    position: absolute; left: 0; top: 418px; width: 469px; height: 68px;
    background: var(--band); color: var(--white);
    display: flex; flex-direction: column; align-items: center; justify-content: center;
    font-size: 15px;
  }
  .back-band .contact-row + .contact-row { margin-top: 6px; }
  .mailing-space { position: absolute; left: 469px; top: 0; width: 363px; height: 518px; background: var(--white); }
</style>
</head>
<body>

<svg width="0" height="0" style="position:absolute">
  <defs>
    <symbol id="icon-phone" viewBox="0 0 20 20">
      <circle cx="10" cy="10" r="8.6" fill="none" stroke="#c81d28" stroke-width="1.6"/>
      <path d="M7 5.5 L8.6 5.3 L9.3 7.6 L8.2 8.5 Q9.2 10.8 11.5 11.8 L12.4 10.7 L14.7 11.4 L14.5 13 Q12 14.6 8.8 12 Q6 9.4 7 5.5 Z" fill="#c81d28"/>
    </symbol>
    <symbol id="icon-fax" viewBox="0 0 20 20">
      <circle cx="10" cy="10" r="8.6" fill="none" stroke="#c81d28" stroke-width="1.6"/>
      <rect x="7" y="5" width="6" height="3.5" fill="#c81d28"/>
      <rect x="5" y="8.5" width="10" height="5" rx="1" fill="#c81d28"/>
      <rect x="7" y="11.5" width="6" height="3.5" fill="#fff" stroke="#c81d28" stroke-width=".8"/>
    </symbol>
    <symbol id="icon-web" viewBox="0 0 20 20">
      <circle cx="10" cy="10" r="8.6" fill="none" stroke="#c81d28" stroke-width="1.6"/>
      <circle cx="10" cy="11" r="4.2" fill="#c81d28"/>
      <path d="M8 5 L10 7 L12 5" fill="none" stroke="#c81d28" stroke-width="1.2"/>
    </symbol>
    <symbol id="icon-pin" viewBox="0 0 20 20">
      <circle cx="10" cy="10" r="8.6" fill="none" stroke="#c81d28" stroke-width="1.6"/>
      <path d="M5.5 10 L10 5.8 L14.5 10 L13.2 10 L13.2 14 L6.8 14 L6.8 10 Z" fill="#c81d28"/>
      <rect x="9" y="11.2" width="2" height="2.8" fill="#fff"/>
    </symbol>
  </defs>
</svg>

<section class="card card-front">
  <div class="front-backdrop" role="img" aria-label="Deep red holiday background with glittering red snowflakes and sparkles"></div>
  <div class="group-photo" role="img" aria-label="Group photo of the clinic's physicians in white coats seated in front and staff in scrubs standing behind"></div>
  <div class="snow-fade"></div>
  <h1 class="greeting">
    <span class="greeting-small">SEASON'S</span>
    <span class="greeting-script">Greetings</span>
  </h1>

  <div class="brand front-brand">
    <span class="brand-dot"></span>
    <span class="brand-name">Tidewater Cardio</span>
  </div>

  <div class="contact front-contact">
    <div class="contact-row">
      <span class="contact-item"><svg class="icon"><use href="#icon-phone"/></svg><span class="strong">832-617-2283</span></span>
      <span class="contact-item"><svg class="icon"><use href="#icon-fax"/></svg><span>832-617-2284</span></span>
    </div>
    <div class="contact-row">
      <span class="contact-item"><svg class="icon"><use href="#icon-web"/></svg><span>www.<span class="strong">tidewatercardio-example</span>.com</span></span>
    </div>
  </div>

  <div class="contact front-address">
    <svg class="icon"><use href="#icon-pin"/></svg>
    <address style="font-style:normal">718 Marwick Ave. Ste. B,<br>Webster, TX 77341</address>
  </div>
</section>

<section class="card card-back">
  <div class="back-panel" role="img" aria-label="Red holiday background with glittering red snowflakes in the upper left"></div>

  <div class="brand back-brand">
    <span class="brand-dot"></span>
    <span class="brand-name">Tidewater Cardio</span>
  </div>

  <div class="back-message">
    <div class="headline">Happy Holidays</div>
    <div class="line line-one">from the Physicians and Staff</div>
    <div class="line line-two">at Tidewater Cardio</div>
  </div>

  <div class="back-band contact">
    <div class="contact-row">
      <span class="contact-item"><svg class="icon"><use href="#icon-phone"/></svg><span class="strong">832-617-2283</span></span>
      <span class="contact-item"><svg class="icon"><use href="#icon-fax"/></svg><span>832-617-2284</span></span>
    </div>
    <div class="contact-row">
      <span class="contact-item"><svg class="icon"><use href="#icon-web"/></svg><span>www.<span class="strong">tidewatercardio-example</span>.com</span></span>
    </div>
  </div>

  <div class="mailing-space"></div>
</section>

</body>
</html>
```